Brusola Card Design Project

Our company,Brusola, is focusing B to B, and people receiving this card are managers or engineers in the handset maker in the world.
Therefore we hope this to be designed strictly serious one but it needs cool and unique style which could imagine something innovation from the card.

This card will be used for Japanese,Chinese and English.
Please consider 2 byte character usage.

It Company

```html
<!DOCTYPE html>
<html lang="en">
<head>
<meta charset="utf-8">
<title>Brusola Business Card</title>
<link href="https://fonts.googleapis.com/css2?family=Arimo:wght@400;700&display=swap" rel="stylesheet">
<style>
  :root {
    --bg-top: #9b9b9b;
    --bg-bottom: #e4e4e4;
    --card: #ffffff;
    --ink-dark: #5a5a5a;
    --ink-mid: #7a7a7a;
    --ink-light: #b5b5b5;
    --emboss: #ececec;
    --strip-top: #ffffff;
    --strip-bottom: #8c8c8c;
    --label: #ffffff;
  }
  * { box-sizing: border-box; margin: 0; padding: 0; }
  html, body { width: 1200px; height: 1131px; overflow: hidden; }
  body {
    position: relative;
    background: linear-gradient(180deg, var(--bg-top) 0%, var(--bg-bottom) 100%);
    font-family: "Arimo", Arial, sans-serif;
  }
  .side-label {
    position: absolute;
    color: var(--label);
    font-weight: 700;
    font-size: 27px;
  }
  .side-label--recto { left: 22px; top: 128px; }
  .side-label--verso { left: 340px; top: 606px; }

  .card {
    position: absolute;
    width: 790px;
    height: 436px;
    background: var(--card);
    border-radius: 30px;
    overflow: hidden;
    box-shadow: 0 6px 14px rgba(0,0,0,0.25);
  }
  .card--front { left: 22px; top: 170px; }
  .card--back { left: 340px; top: 652px; }

  .brand {
    position: absolute;
    display: flex;
    align-items: center;
    gap: 14px;
    font-weight: 700;
    letter-spacing: 1px;
  }
  .brand__dot { border-radius: 50%; }

  .card--front .brand { left: 70px; top: 180px; font-size: 50px; color: var(--ink-dark); }
  .card--front .brand__dot { width: 34px; height: 34px; background: var(--ink-dark); }

  .divider {
    position: absolute;
    left: 400px; top: 95px;
    width: 1px; height: 170px;
    background: var(--ink-light);
  }
  .identity { position: absolute; left: 440px; top: 100px; color: var(--ink-mid); font-size: 15px; line-height: 1.3; }
  .identity__name { font-weight: 700; color: var(--ink-dark); font-size: 16px; }
  .identity__role { text-transform: uppercase; }
  .identity__address { margin-top: 36px; }

  .contact-strip {
    position: absolute;
    left: 0; right: 0; bottom: 0;
    height: 90px;
    background: linear-gradient(180deg, var(--strip-top) 0%, var(--strip-bottom) 100%);
    display: flex;
    align-items: flex-end;
    padding: 0 0 14px 34px;
    color: #f2f2f2;
    font-size: 11.5px;
    letter-spacing: 3px;
    white-space: nowrap;
  }

  .card--back .brand { left: 50%; top: 170px; transform: translateX(-50%); font-size: 56px; color: var(--emboss); }
  .card--back .brand__dot { width: 38px; height: 38px; background: var(--emboss); }
  .web { position: absolute; right: 56px; bottom: 38px; color: var(--ink-mid); font-size: 15px; }
</style>
</head>
<body>
  <div class="side-label side-label--recto">Recto</div>
  <section class="card card--front">
    <div class="brand"><span class="brand__dot"></span>BRUSOLA</div>
    <div class="divider"></div>
    <div class="identity">
      <div class="identity__name">DANIEL HART</div>
      <div class="identity__role">Managing Director</div>
      <div class="identity__address">14 Elmfield Yard, Mill Lane,<br>Ashbury Wessex AB12 3CD<br>England</div>
    </div>
    <div class="contact-strip">Telephone: (212) 555-0148 | Fax: (212) 555-0149 | email: danielhart@brusola.com</div>
  </section>

  <div class="side-label side-label--verso">verso with emboss on logo</div>
  <section class="card card--back">
    <div class="brand"><span class="brand__dot"></span>BRUSOLA</div>
    <div class="web">www.brusola.com</div>
  </section>
</body>
</html>
```